PostCard for Managed IT Services

We need a postcard design for a postcard that we intend to send out early in our marketing efforts to medical practices. The postcard should communicate our core services for small businesses including 1.) Managed IT Services, 2.) Security Services, 3.) Cloud Services, and 4.) IT Project and Integration work. company information is available at www.fernwaylab.com. I attached a two logos.WHILE WE WANT TO USE THE LOGO AND COLORS FROM OUR SITE, I HOPE THE DESIGN IS BOLD AND GRABS ATTENTION. I HOPE IT IS NOT THE 'SAME OLD' INFORMATION TECHNOLOGY LOOK. BE CREATIVE AND GET THE READER TO LOOK TWICE.

Target Market(s)

Businesses, medical practices

Font styles to use
Serif
Sans Serif

Requirements
Must have
• We need to include somewhere that are technicians are trained in on plain badge shape and PCI (see site for info on the two)

```html
<!DOCTYPE html>
<html lang="en">
<head>
<meta charset="utf-8">
<title>Fernway Lab Postcard</title>
<link href="https://fonts.googleapis.com/css2?family=Roboto+Condensed:ital,wght@0,400;0,700;1,400&family=Roboto:wght@300;400;700&display=swap" rel="stylesheet">
<style>
:root{
  --page:#eceef1;
  --white:#ffffff;
  --green:#3db54a;
  --blue:#2d4f9f;
  --navy:#0e1c48;
  --ink-bar:#1f2226;
  --text-dark:#2a2a2a;
  --line:#9aa0a8;
}
*{box-sizing:border-box;margin:0;padding:0}
html,body{width:689px;height:1200px;overflow:hidden;background:var(--page)}
body{position:relative;font-family:"Roboto Condensed",Arial,sans-serif}
.postcard{position:absolute;left:34px;width:620px;height:415px;background:var(--white);overflow:hidden;box-shadow:0 4px 14px rgba(0,0,0,.18)}
.postcard--front{top:165px}
.postcard--back{top:625px}
.layer{position:absolute;left:0;top:0}

/* front */
.brand{position:absolute;display:flex;align-items:center;gap:6px;color:var(--blue);font-family:"Roboto Condensed",sans-serif;font-weight:700;letter-spacing:2px}
.brand__dot{width:10px;height:10px;border-radius:50%;background:var(--blue)}
.postcard--front .brand{left:432px;top:66px;font-size:15px}
.headline{position:absolute;left:328px;top:142px;width:284px;height:70px;background:var(--green);color:var(--white);font-family:"Roboto",Arial,sans-serif;font-weight:300;font-size:19px;line-height:23px;padding:12px 0 0 34px}
.headline b{font-weight:700}
.services{position:absolute;left:352px;top:212px;width:260px;height:153px;background:var(--blue);list-style:none;padding:10px 0 0 16px}
.services li{display:flex;align-items:center;gap:12px;height:35px;color:var(--white);font-size:14px}
.services svg{flex:none}
.contact-bar{position:absolute;left:346px;top:365px;width:266px;height:40px;background:var(--ink-bar);display:flex;align-items:center;padding-left:14px;gap:8px;color:var(--white)}
.phone{display:flex;align-items:center;gap:6px;font-size:14px;font-weight:700}
.divider{width:1px;height:24px;background:var(--line)}
.links{font-size:10.5px;line-height:13px}
.links span{color:var(--green)}

/* back */
.about{position:absolute;left:16px;top:28px;width:290px;color:var(--white)}
.about__title{color:var(--green);font-size:24px;font-weight:700;margin-bottom:8px}
.about__body{font-size:11.5px;line-height:15px}
.about__note{font-size:11.5px;font-style:italic;margin-top:14px}
.trained{position:absolute;left:96px;top:239px;width:150px;height:25px;border:1px solid var(--green);color:var(--green);font-size:18px;font-weight:700;text-align:center;line-height:23px}
.trained::before,.trained::after{content:"";position:absolute;top:11px;width:70px;height:1px;background:var(--line)}
.trained::before{right:100%}
.trained::after{left:100%}
.badges{position:absolute;left:24px;top:280px;display:flex;align-items:center;gap:18px}
.badge-shape{background:var(--white)}
.badge-shape--rect{width:64px;height:34px;border-radius:4px}
.badge-shape--circle{width:42px;height:42px;border-radius:50%}
.badges .divider{height:48px;background:#7f8ab0}
.back-contacts{position:absolute;left:10px;top:370px;display:flex;align-items:center;gap:8px;color:var(--text-dark)}
.back-contacts .phone{font-weight:400}
.back-contacts .divider{background:#555}
.brand-block{position:absolute;left:360px;top:30px;text-align:center}
.brand-block .brand{position:static;font-size:12px;justify-content:center}
.brand-block__tag{color:var(--blue);font-size:6px;letter-spacing:1.5px;margin-top:4px;line-height:8px}
.stamp{position:absolute;left:530px;top:24px;width:70px;height:64px;border:1px solid #444}
.address-line{position:absolute;left:398px;width:202px;height:1px;background:#555}
</style>
</head>
<body>

<section class="postcard postcard--front" aria-label="Postcard front">
  <svg class="layer" width="620" height="415" viewBox="0 0 620 415">
    <defs>
      <radialGradient id="techGlow" cx="0.6" cy="0.72" r="0.75">
        <stop offset="0" stop-color="#ffd36a"/>
        <stop offset="0.18" stop-color="#e47b2c"/>
        <stop offset="0.45" stop-color="#3c5a8f"/>
        <stop offset="1" stop-color="#101a3a"/>
      </radialGradient>
    </defs>
    <circle cx="150" cy="236" r="200" fill="url(#techGlow)" role="img" aria-label="Photo of a hand touching a glowing tablet with a circuit of technology icons"/>
    <path d="M 0 34 A 250 250 0 0 1 250 34" fill="none" stroke="var(--green)" stroke-width="6" transform="translate(0,12)"/>
    <path d="M 20 40 A 230 230 0 0 1 260 50" fill="none" stroke="var(--blue)" stroke-width="1.5"/>
    <path d="M 300 90 A 214 214 0 0 1 335 390" fill="none" stroke="var(--blue)" stroke-width="2"/>
    <path d="M 318 110 A 222 222 0 0 1 318 405" fill="none" stroke="var(--green)" stroke-width="4" stroke-dasharray="60 40 120 30"/>
  </svg>

  <div class="brand"><span class="brand__dot"></span>Fernway Lab</div>

  <h1 class="headline">Partner With <b>The Best</b><br>For <b>All Your It Needs!</b></h1>

  <ul class="services">
    <li><svg width="22" height="22" viewBox="0 0 22 22"><circle cx="11" cy="11" r="10" fill="#fff"/><circle cx="11" cy="11" r="4" fill="none" stroke="var(--blue)" stroke-width="2"/></svg>Managed IT Services</li>
    <li><svg width="22" height="22" viewBox="0 0 22 22"><circle cx="11" cy="11" r="10" fill="#fff"/><rect x="7" y="10" width="8" height="6" fill="var(--blue)"/><path d="M8.5 10V8a2.5 2.5 0 0 1 5 0v2" fill="none" stroke="var(--blue)" stroke-width="1.5"/></svg>Security Services</li>
    <li><svg width="22" height="22" viewBox="0 0 22 22"><circle cx="11" cy="11" r="10" fill="#fff"/><path d="M6 14h10a2.5 2.5 0 0 0 0-5 3.5 3.5 0 0 0-6.7-1A3 3 0 0 0 6 14z" fill="var(--blue)"/></svg>Cloud Services</li>
    <li><svg width="22" height="22" viewBox="0 0 22 22"><circle cx="11" cy="11" r="10" fill="#fff"/><rect x="7" y="6" width="8" height="10" fill="none" stroke="var(--blue)" stroke-width="1.5"/><path d="M9 9h4M9 12h4" stroke="var(--blue)"/></svg>IT Project and Integration work</li>
  </ul>

  <div class="contact-bar">
    <span class="phone"><svg width="12" height="12" viewBox="0 0 24 24"><path d="M6.6 10.8a15 15 0 0 0 6.6 6.6l2.2-2.2a1 1 0 0 1 1-.25 11.4 11.4 0 0 0 3.6.57 1 1 0 0 1 1 1V20a1 1 0 0 1-1 1A17 17 0 0 1 3 4a1 1 0 0 1 1-1h3.5a1 1 0 0 1 1 1c0 1.25.2 2.45.57 3.57a1 1 0 0 1-.25 1z" fill="var(--green)"/></svg>(555) 014-2237</span>
    <span class="divider"></span>
    <span class="links">info@<span>fernwaylab</span>.com<br>www.<span>fernwaylab</span>.com</span>
  </div>
</section>

<section class="postcard postcard--back" aria-label="Postcard back">
  <svg class="layer" width="620" height="415" viewBox="0 0 620 415">
    <defs>
      <linearGradient id="keyboardTone" x1="0" y1="0" x2="0.3" y2="1">
        <stop offset="0" stop-color="#0b1436"/>
        <stop offset="0.6" stop-color="#1d3577"/>
        <stop offset="1" stop-color="#2a4ea0"/>
      </linearGradient>
    </defs>
    <path d="M0 0 H292 C345 70 352 250 250 356 H0 Z" fill="url(#keyboardTone)" role="img" aria-label="Dark blue photo of a computer keyboard"/>
    <path d="M300 4 C356 74 362 258 258 366" fill="none" stroke="var(--green)" stroke-width="4"/>
    <path d="M312 30 C360 110 356 270 280 370" fill="none" stroke="var(--blue)" stroke-width="2"/>
    <path d="M340 160 C345 250 320 330 270 390" fill="none" stroke="var(--blue)" stroke-width="1.5"/>
  </svg>

  <div class="about">
    <h2 class="about__title">About Us</h2>
    <p class="about__body">To be competitive in today's economy, businesses need cost-effective IT consulting services they can count on. Fernway Lab believes in being long-term partners with our clients by providing proactive and hassle free Managed IT Services, IT Consulting and Cloud Services.</p>
    <p class="about__note">We serve all industries.</p>
  </div>

  <div class="trained">Trained in On</div>
  <div class="badges">
    <span class="badge-shape badge-shape--rect"></span>
    <span class="divider"></span>
    <span class="badge-shape badge-shape--circle"></span>
  </div>

  <div class="back-contacts">
    <span class="phone"><svg width="12" height="12" viewBox="0 0 24 24"><path d="M6.6 10.8a15 15 0 0 0 6.6 6.6l2.2-2.2a1 1 0 0 1 1-.25 11.4 11.4 0 0 0 3.6.57 1 1 0 0 1 1 1V20a1 1 0 0 1-1 1A17 17 0 0 1 3 4a1 1 0 0 1 1-1h3.5a1 1 0 0 1 1 1c0 1.25.2 2.45.57 3.57a1 1 0 0 1-.25 1z" fill="var(--green)"/></svg>(555) 014-2237</span>
    <span class="divider"></span>
    <span class="links">info@<span>fernwaylab</span>.com<br>www.<span>fernwaylab</span>.com</span>
  </div>

  <div class="brand-block">
    <div class="brand"><span class="brand__dot"></span>Fernway Lab</div>
    <p class="brand-block__tag">Managed Services<br>Partner with the best</p>
  </div>

  <div class="stamp"></div>
  <span class="address-line" style="top:240px"></span>
  <span class="address-line" style="top:280px"></span>
  <span class="address-line" style="top:319px"></span>
</section>

</body>
</html>
```